Managed Service Provider email

We need an email designed that advertises our Managed Services product. We have been in business 28 years. Managed Services includes proactive ticketing, Help desk support, server and workstation monitoring, data backup monitoring, spam protection, regular reports, Deskflow 240, telecom services, ISP management, vendor management and more.

Target Market(s)

Business owners, decision makers, IT, CTO

Industry/Entity Type

Information Technology

Colors

Designer to choose colors to be used in the design.

Requirements
Must have
• Bullet points with included services. Mention of 28 years in business.
Nice to have
• We'd love our designer to read up on what an MSP (Managed Service Provider) does and use that information to find/create content for our email project.
Should not have
• A picture of a computer with a thermometer in its mouth.

```html
<!DOCTYPE html>
<html lang="en">
<head>
<meta charset="utf-8">
<title>Keltra Network Services – Managed Services</title>
<link href="https://fonts.googleapis.com/css2?family=Exo+2:wght@700;800&family=Open+Sans:wght@400;600;700&display=swap" rel="stylesheet">
<style>
  :root {
    --brand-blue: #1e88e0;
    --ink: #262626;
    --body-text: #6b6b6b;
    --page: #fafafa;
    --white: #ffffff;
    --footer: #2a2a2a;
    --badge-border: #dcdcdc;
  }
  * { margin: 0; padding: 0; box-sizing: border-box; }
  html, body { width: 1200px; height: 2507px; overflow: hidden; }
  body {
    background: var(--page);
    font-family: "Open Sans", Arial, sans-serif;
    color: var(--ink);
    position: relative;
  }

  /* Hero */
  .hero {
    position: absolute; left: 0; top: 0; width: 1200px; height: 585px;
    background:
      radial-gradient(ellipse 520px 520px at 200px 260px, rgba(214,170,150,0.9), rgba(214,170,150,0) 70%),
      linear-gradient(100deg, #6a4a3a 0%, #b98d78 30%, #c9a794 55%, #b69a8c 78%, #8e7668 100%);
  }
  .hero-shade { position: absolute; inset: 0; background: rgba(20,20,30,0.18); }
  .brand {
    position: absolute; left: 0; width: 1200px; top: 140px;
    text-align: center; color: var(--white); font-weight: 700;
  }
  .brand-name { font-size: 150px; line-height: 1; letter-spacing: 2px; }
  .brand-tagline { font-size: 40px; line-height: 1.2; margin-top: 6px; letter-spacing: 2px; }
  .hero-years {
    position: absolute; left: 0; width: 1200px; top: 372px;
    text-align: center; color: var(--white);
    font-size: 60px; font-weight: 700; letter-spacing: 1px;
  }

  /* Headings */
  .section-title {
    position: absolute; left: 0; width: 1200px; text-align: center;
    font-family: "Exo 2", Arial, sans-serif; font-weight: 800;
    text-transform: uppercase; letter-spacing: 2px;
  }
  .welcome-title { top: 655px; font-size: 74px; }
  .welcome-text {
    position: absolute; left: 115px; width: 970px; top: 772px;
    text-align: center; font-size: 25px; line-height: 55px; color: var(--body-text);
  }

  /* Services */
  .services {
    position: absolute; left: 92px; top: 1056px; width: 1016px; height: 662px;
    background: var(--brand-blue); border-radius: 7px; color: var(--white);
  }
  .services-title { top: 95px; width: 1016px; font-size: 60px; color: var(--white); }
  .service-list { list-style: none; position: absolute; top: 230px; width: 420px; }
  .service-list.col-left { left: 58px; }
  .service-list.col-right { left: 652px; }
  .service-item {
    display: flex; align-items: center; height: 77.5px;
    font-size: 28px; font-weight: 400;
  }
  .service-item svg { width: 26px; height: 26px; margin-right: 22px; flex: none; }

  /* Partners */
  .partners-title { top: 1800px; font-size: 68px; }
  .partner-badge {
    position: absolute; top: 1940px; width: 237px; height: 126px;
    background: var(--white); border: 2px solid var(--badge-border); border-radius: 5px;
    display: flex; align-items: center; justify-content: center;
  }
  .partner-badge span { display: block; width: 130px; height: 40px; border-radius: 4px; background: #e3e7ec; }
  .partner-badge.alt { background: #eceff2; }
  .partner-badge.alt span { background: #d3dae2; }

  /* Footer */
  .footer {
    position: absolute; left: 0; top: 2161px; width: 1200px; height: 346px;
    background: var(--footer); color: var(--white);
  }
  .social-link {
    position: absolute; top: 88px; width: 87px; height: 87px;
    border: 3px solid var(--white); border-radius: 50%;
  }
  .social-link::after {
    content: ""; position: absolute; left: 31px; top: 31px; width: 19px; height: 19px;
    background: var(--white); border-radius: 50%;
  }
  .footer-legal {
    position: absolute; left: 0; width: 1200px; top: 224px;
    text-align: center; font-size: 26px;
  }
</style>
</head>
<body>

  <header class="hero" role="img" aria-label="Photo of a smiling support agent wearing a headset">
    <div class="hero-shade"></div>
    <div class="brand">
      <div class="brand-name">Keltra</div>
      <div class="brand-tagline">network services</div>
    </div>
    <div class="hero-years">28 YEARS IN BUSINESS</div>
  </header>

  <h1 class="section-title welcome-title">Welcome!</h1>
  <p class="welcome-text">
    At vero eos et accusamus et iusto odio dignissimos ducimus qui blanditiis prae-
    sentium voluptatum deleniti atque corrupti quos dolores et quas molestias
    excepturi sint occaecati cupiditate non providentsimilique sunt in culpa qui
    officia deserunt mollitia animid est laborum et dolorum fuga
  </p>

  <section class="services">
    <h2 class="section-title services-title">Our Services</h2>
    <svg width="0" height="0" style="position:absolute">
      <symbol id="tick-box" viewBox="0 0 26 26">
        <rect x="2" y="5" width="19" height="19" rx="3" fill="none" stroke="#fff" stroke-width="3"/>
        <path d="M7 13 l5 5 L24 4" fill="none" stroke="#fff" stroke-width="3.4" stroke-linecap="round" stroke-linejoin="round"/>
      </symbol>
    </svg>
    <ul class="service-list col-left">
      <li class="service-item"><svg><use href="#tick-box"/></svg>Proactive ticketing</li>
      <li class="service-item"><svg><use href="#tick-box"/></svg>Help desk support</li>
      <li class="service-item"><svg><use href="#tick-box"/></svg>Server and workstation monitoring</li>
      <li class="service-item"><svg><use href="#tick-box"/></svg>Data backup monitoring</li>
      <li class="service-item"><svg><use href="#tick-box"/></svg>Spam protection</li>
    </ul>
    <ul class="service-list col-right">
      <li class="service-item"><svg><use href="#tick-box"/></svg>Regular reports</li>
      <li class="service-item"><svg><use href="#tick-box"/></svg>Deskflow 240</li>
      <li class="service-item"><svg><use href="#tick-box"/></svg>Telecom services</li>
      <li class="service-item"><svg><use href="#tick-box"/></svg>ISP management</li>
      <li class="service-item"><svg><use href="#tick-box"/></svg>Vendor management</li>
    </ul>
  </section>

  <h2 class="section-title partners-title">Our Partners</h2>
  <div class="partner-badge" style="left:107px" aria-label="Partner badge"><span></span></div>
  <div class="partner-badge alt" style="left:357px" aria-label="Partner badge"><span></span></div>
  <div class="partner-badge" style="left:608px" aria-label="Partner badge"><span></span></div>
  <div class="partner-badge" style="left:857px" aria-label="Partner badge"><span></span></div>

  <footer class="footer">
    <a class="social-link" style="left:314px" aria-label="Social link"></a>
    <a class="social-link" style="left:411px" aria-label="Social link"></a>
    <a class="social-link" style="left:508px" aria-label="Social link"></a>
    <a class="social-link" style="left:605px" aria-label="Social link"></a>
    <a class="social-link" style="left:702px" aria-label="Social link"></a>
    <a class="social-link" style="left:799px" aria-label="Social link"></a>
    <p class="footer-legal">Copyrights © 2018, Keltra. All rights reserved.&nbsp; Sitemap | Terms | Privacy</p>
  </footer>

</body>
</html>
```